Geschäftspapiere für Rechtsberatung
Zielgruppe
Rechtsberatung; Zielgruppe sind sowohl Privat- als auch Geschäftsleute
Die Einzelkanzlei von Marlene Kosswig (Näheres siehe www.kosswig-beispiel.de) wird zu einer Partnergesellschaft, der
Kosswig

```html
<!DOCTYPE html>
<html lang="de">
<head>
<meta charset="utf-8">
<title>Briefbogen – Rechtsanwaltskanzlei Marlene Kosswig</title>
<link rel="stylesheet" href="https://fonts.googleapis.com/css2?family=Crimson+Pro:wght@400;600&display=swap">
<style>
  :root {
    --band: #b05a4a;
    --brand-red: #9b1b22;
    --ink: #1d1d1d;
    --ink-soft: #5a5a5a;
    --paper: #ffffff;
    --backdrop: #ececec;
    --mark: #b8b8b8;
  }
  * { box-sizing: border-box; margin: 0; padding: 0; }
  html, body {
    width: 1200px; height: 861px; overflow: hidden;
    background: var(--backdrop);
    font-family: "Crimson Pro", Georgia, serif;
    color: var(--ink-soft);
  }
  .letterhead {
    position: absolute; left: 302px; top: 10px;
    width: 595px; height: 841px;
    background: var(--paper);
    box-shadow: 0 2px 10px rgba(0,0,0,.12);
  }
  .top-band { position: absolute; left: 0; top: 0; width: 595px; height: 60px; }
  .brand {
    position: absolute; left: 0; top: 86px; width: 595px;
    text-align: center; color: var(--ink); font-weight: 400; line-height: 1.05;
  }
  .brand-kind { font-size: 12px; letter-spacing: .2px; }
  .brand-name { font-size: 17px; }
  .sender-line {
    position: absolute; left: 57px; top: 156px;
    font-size: 8.5px; color: var(--ink);
  }
  .sender-line .firm { color: var(--brand-red); font-weight: 600; }
  .reference {
    position: absolute; left: 394px; top: 154px;
    font-size: 10.5px; line-height: 17px; color: var(--ink-soft);
  }
  .fold-mark { position: absolute; left: 0; height: 1px; background: var(--mark); }
  .fold-mark.upper { top: 298px; width: 8px; }
  .fold-mark.punch { top: 421px; left: 33px; width: 18px; }
  .fold-mark.lower { top: 596px; width: 8px; }
  .footer {
    position: absolute; top: 746px; left: 57px; right: 40px;
    display: flex; font-size: 10.5px; line-height: 14px; color: var(--ink-soft);
  }
  .footer-firm { width: 199px; }
  .footer-firm strong { color: var(--ink); font-weight: 600; display: block; }
  .footer-firm .address { margin-top: 6px; }
  .footer-contact { width: 155px; }
  .footer-bank { flex: 1; }
  .row { display: flex; }
  .row .label { width: 34px; }
  .footer-bank .row .label { width: 54px; }
  .gap { height: 6px; }
  .bottom-band {
    position: absolute; left: 0; bottom: 0; width: 595px; height: 10px;
    background: var(--brand-red);
  }
</style>
</head>
<body>
  <main class="letterhead">
    <svg class="top-band" viewBox="0 0 595 60" aria-hidden="true">
      <polygon points="0,0 595,0 595,40 345,40 330,12 265,12 250,40 0,40" fill="var(--band)"/>
      <rect x="284" y="38" width="26" height="26" fill="var(--brand-red)"/>
    </svg>

    <header class="brand">
      <div class="brand-kind">Rechtsanwaltskanzlei</div>
      <div class="brand-name">Marlene Kosswig</div>
    </header>

    <p class="sender-line"><span class="firm">Kosswig § Brenner PartG mbB</span> • Lindenweg 14 • 45100 Musterstadt</p>

    <div class="reference">
      <div>Datum:</div>
      <div>Unser Zeichen:</div>
    </div>

    <span class="fold-mark upper"></span>
    <span class="fold-mark punch"></span>
    <span class="fold-mark lower"></span>

    <footer class="footer">
      <div class="footer-firm">
        <strong>Kosswig § Brenner PartG mbB</strong>
        <strong>Marlene Kosswig</strong>
        <div class="address">Dipl.-Juristin<br>Lindenweg 14<br>45100 Musterstadt</div>
      </div>
      <div class="footer-contact">
        <div class="row"><span class="label">Tel.:</span>0201/5550100</div>
        <div class="row"><span class="label">Fax:</span>0201/5550102</div>
        <div class="row"><span class="label">Mobil:</span>0170/5550103</div>
        <div class="gap"></div>
        <div class="row"><span class="label">Mail:</span>info@kosswig-beispiel.de</div>
        <div class="row"><span class="label">Web:</span>www.kosswig-beispiel.de</div>
      </div>
      <div class="footer-bank">
        <div>Nordfeld Bank</div>
        <div class="row"><span class="label">IBAN:</span>DE00 1234 5678<br>9012 3456 78</div>
        <div class="row"><span class="label">BIC:</span>NORDDEX 1XX</div>
        <div class="gap"></div>
        <div class="row"><span class="label">Steuer-Nr.</span>XXX XXX XXX XXX</div>
      </div>
    </footer>

    <div class="bottom-band"></div>
  </main>
</body>
</html>
```